Maple Hollow Bloom Backdrops Business card

Looking to have a business card design incorporating my logo for my flower wall business.

Industry/Entity Type

Wedding & event planning

Contact Information for Business Card

My business logo, my name - Jill Worthing (owner), my tagline - Let us be your something extra, phone # 401-627-3918, email address - maplehollowbloombackdrops@fernpost.com, my website - maplehollowbloombackdrops.com, Instagram handle- @maplehollowbloombackdrops, FB handle Handle - maplehollowbloombackdrops

Font styles to use
Other font styles liked:
• Sentaina is the font that is used in my logo

Requirements
Must have
• Would like a double sided business card

```html
<!DOCTYPE html>
<html lang="en">
<head>
<meta charset="utf-8">
<title>Maple Hollow Bloom Backdrops – Business Card</title>
<link href="https://fonts.googleapis.com/css2?family=Great+Vibes&family=Roboto:wght@400&display=swap" rel="stylesheet">
<style>
  :root {
    --backdrop: #d4d4d4;
    --card-pink: #fadde7;
    --card-edge: #e394c4;
    --ink: #2a2a2a;
    --accent-pink: #e58bbd;
    --logo-white: #ffffff;
    --gold: #d9b45a;
  }
  * { margin: 0; padding: 0; box-sizing: border-box; }
  html, body { width: 1200px; height: 913px; overflow: hidden; }
  body { background: var(--backdrop); position: relative; font-family: "Roboto", Arial, sans-serif; color: var(--ink); }

  .card {
    position: absolute;
    top: 302px;
    width: 540px;
    height: 309px;
    background: var(--card-pink);
    border: 2px solid var(--card-edge);
  }
  .card--front { left: 40px; }
  .card--back { left: 620px; }

  .logo-badge {
    position: absolute;
    border-radius: 50%;
    background: var(--logo-white);
    border: 1.5px solid var(--gold);
    display: flex;
    align-items: center;
    justify-content: center;
    text-align: center;
    color: var(--ink);
    font-family: "Roboto", Arial, sans-serif;
    font-weight: 400;
    line-height: 1.25;
  }
  .card--front .logo-badge { width: 130px; height: 130px; right: 36px; top: 22px; font-size: 14px; padding: 16px; }
  .card--back .logo-badge { width: 212px; height: 212px; left: 164px; top: 48px; font-size: 22px; padding: 26px; }

  .owner { position: absolute; left: 40px; top: 112px; }
  .owner__name { font-family: "Great Vibes", cursive; font-size: 36px; line-height: 1; }
  .owner__role { font-family: "Great Vibes", cursive; font-size: 22px; margin-left: 18px; }

  .divider { position: absolute; left: 30px; right: 58px; top: 196px; height: 1.5px; background: var(--ink); }

  .contacts { position: absolute; left: 30px; top: 212px; list-style: none; }
  .contacts li, .socials li { display: flex; align-items: center; gap: 8px; font-size: 12.5px; height: 24px; }
  .socials { position: absolute; left: 328px; top: 212px; list-style: none; }
  .socials li { font-size: 12px; }

  .icon { width: 14px; height: 14px; flex: none; }
  .icon-square { width: 12px; height: 12px; background: var(--accent-pink); flex: none; }
</style>
</head>
<body>

  <section class="card card--front" aria-label="Business card front">
    <div class="logo-badge">Maple Hollow Bloom Backdrops</div>

    <div class="owner">
      <p class="owner__name">Jill Worthing</p>
      <p class="owner__role">owner</p>
    </div>

    <div class="divider"></div>

    <ul class="contacts">
      <li>
        <svg class="icon" viewBox="0 0 14 14"><path d="M3 1h2.5l1 3-1.6 1.2a7 7 0 0 0 3.9 3.9L10 7.5l3 1V11a2 2 0 0 1-2 2A10 10 0 0 1 1 3a2 2 0 0 1 2-2z" fill="var(--accent-pink)"/></svg>
        401-627-3918
      </li>
      <li>
        <svg class="icon" viewBox="0 0 14 14"><rect x="1" y="3" width="12" height="8" fill="var(--accent-pink)"/><path d="M1 3l6 4.5L13 3" fill="none" stroke="#fff" stroke-width="1"/></svg>
        maplehollowbloombackdrops@fernpost.com
      </li>
      <li>
        <svg class="icon" viewBox="0 0 14 14"><circle cx="7" cy="7" r="6" fill="var(--accent-pink)"/><path d="M1 7h12M7 1c-2.5 3-2.5 9 0 12M7 1c2.5 3 2.5 9 0 12" fill="none" stroke="#fff" stroke-width="0.8"/></svg>
        maplehollowbloombackdrops.com
      </li>
    </ul>

    <ul class="socials">
      <li><span class="icon-square"></span>maplehollowbloombackdrops</li>
      <li><span class="icon-square"></span>@maplehollowbloombackdrops</li>
    </ul>
  </section>

  <section class="card card--back" aria-label="Business card back">
    <div class="logo-badge">Maple Hollow Bloom Backdrops</div>
  </section>

</body>
</html>
```